GRA Stationary
GRA, Garnet Resale Advisors
Professional
Dominic T. Harlow
P.O. box 382
Alder Glen, Pa 19507
dtharlow@graadvllc.com
graadvllc.com
I'm open to all ideas. GRA specializes in estate or antique jewelry. So a period approach(Victorian, deco, etc.) might work. But I also like a clean, modern look as well. Color scheme will probably revolve around platinum, but again, I'm open to ideas. Thanks!
needs to have business card, letterhead, fax, and envelope design
logo vector file
KX Press business card format
RGB Color Chart
GRA logo

```html
<!DOCTYPE html>
<html lang="en">
<head>
<meta charset="utf-8">
<title>GRA Stationary – Business Card</title>
<link href="https://fonts.googleapis.com/css2?family=Cinzel:wght@500&family=Great+Vibes&family=Cormorant+Garamond:ital,wght@0,500;1,600&family=Lato:wght@400&display=swap" rel="stylesheet">
<style>
  :root {
    --backdrop: #6b6b6d;
    --card: #ffffff;
    --platinum: #8f9196;
    --platinum-light: #c4c6ca;
    --band: #717378;
    --band-text: #ffffff;
    --ink: #55575c;
    --ornament-light: #eceded;
    --ornament-dark: #b3b5b9;
  }
  * { box-sizing: border-box; margin: 0; padding: 0; }
  html, body { width: 1200px; height: 876px; overflow: hidden; }
  body {
    background: var(--backdrop);
    position: relative;
    font-family: "Lato", sans-serif;
    color: var(--ink);
  }
  .card {
    position: absolute;
    width: 560px;
    height: 320px;
    background: var(--card);
    overflow: hidden;
  }
  .card--contact { left: 90px; top: 90px; }
  .card--front { left: 550px; top: 466px; }

  .logo {
    display: flex;
    align-items: center;
    justify-content: center;
    gap: 10px;
  }
  .logo__mark {
    width: 14px; height: 14px;
    border-radius: 50%;
    background: var(--platinum-light);
  }
  .logo__name {
    font-family: "Cinzel", serif;
    font-weight: 500;
    color: var(--platinum);
    letter-spacing: 2px;
    line-height: 1;
  }
  .company {
    font-family: "Great Vibes", cursive;
    color: var(--platinum);
    text-align: center;
    line-height: 1;
  }

  /* contact side */
  .card--contact .logo { position: absolute; top: 28px; left: 0; right: 0; }
  .card--contact .logo__name { font-size: 40px; }
  .card--contact .company { position: absolute; top: 82px; left: 0; right: 0; font-size: 28px; }
  .name-band {
    position: absolute;
    left: 0; right: 0; top: 128px;
    height: 48px;
    background: var(--band);
    color: var(--band-text);
    text-align: center;
    padding-top: 5px;
  }
  .name-band__name {
    font-family: "Cormorant Garamond", serif;
    font-style: italic;
    font-weight: 600;
    font-size: 20px;
    line-height: 22px;
  }
  .name-band__title { font-size: 11px; line-height: 14px; letter-spacing: .5px; }
  .flourish {
    position: absolute;
    background: linear-gradient(135deg, var(--ornament-light), var(--ornament-dark));
    opacity: .85;
  }
  .flourish--band-left { left: 0; top: 176px; width: 100px; height: 30px; border-bottom-right-radius: 30px; }
  .flourish--band-right { right: 0; top: 102px; width: 90px; height: 26px; border-top-left-radius: 26px; }
  .contact {
    position: absolute;
    left: 0; right: 0; top: 198px;
    text-align: center;
    font-size: 12.5px;
    line-height: 22px;
  }
  .contact__row { display: flex; justify-content: center; gap: 14px; align-items: center; }
  .contact__item { display: inline-flex; align-items: center; gap: 4px; }
  .icon { width: 11px; height: 11px; fill: var(--ink); }

  /* front side */
  .side-band {
    position: absolute;
    right: 0; top: 0; bottom: 0;
    width: 40px;
    background: var(--band);
  }
  .flourish--corner { right: 0; top: 0; width: 120px; height: 150px; border-bottom-left-radius: 120px; }
  .card--front .logo { position: absolute; top: 100px; left: 0; right: 40px; }
  .card--front .logo__name { font-size: 52px; }
  .card--front .logo__mark { width: 18px; height: 18px; }
  .card--front .company { position: absolute; top: 172px; left: 0; right: 40px; font-size: 38px; }
</style>
</head>
<body>

  <section class="card card--contact">
    <div class="logo">
      <span class="logo__mark"></span>
      <span class="logo__name">GRA</span>
    </div>
    <p class="company">Garnet Resale Advisors</p>
    <div class="flourish flourish--band-right" role="img" aria-label="Silver scroll ornament"></div>
    <div class="name-band">
      <p class="name-band__name">Dominic T. Harlow</p>
      <p class="name-band__title">President</p>
    </div>
    <div class="flourish flourish--band-left" role="img" aria-label="Silver scroll ornament"></div>
    <div class="contact">
      <p>P.O. box 382, Alder Glen, Pa 19507</p>
      <p class="contact__row">
        <span class="contact__item"><svg class="icon" viewBox="0 0 12 12"><path d="M2 1h3l1 3-2 1a7 7 0 0 0 3 3l1-2 3 1v3a1 1 0 0 1-1 1A10 10 0 0 1 1 2a1 1 0 0 1 1-1z"/></svg>(888) 555 0143</span>
        <span class="contact__item"><svg class="icon" viewBox="0 0 12 12"><rect x="1" y="4" width="10" height="7" rx="1"/><rect x="3" y="1" width="6" height="3" fill="none" stroke="#55575c"/></svg>(610) 555 0187</span>
        <span class="contact__item"><svg class="icon" viewBox="0 0 12 12"><rect x="3" y="0" width="6" height="12" rx="1"/></svg>(610) 555 0129</span>
      </p>
      <p class="contact__row">
        <span class="contact__item"><svg class="icon" viewBox="0 0 12 12"><rect x="0" y="2" width="12" height="8"/><path d="M0 2l6 5 6-5" fill="none" stroke="#fff"/></svg>dtharlow@graadvllc.com</span>
        <span class="contact__item"><svg class="icon" viewBox="0 0 12 12"><circle cx="6" cy="6" r="5.5"/><path d="M0.5 6h11M6 0.5c-3 3-3 8 0 11M6 0.5c3 3 3 8 0 11" fill="none" stroke="#fff" stroke-width=".8"/></svg>www.graadvllc.com</span>
      </p>
    </div>
  </section>

  <section class="card card--front">
    <div class="side-band"></div>
    <div class="flourish flourish--corner" role="img" aria-label="Silver scroll ornament"></div>
    <div class="logo">
      <span class="logo__mark"></span>
      <span class="logo__name">GRA</span>
    </div>
    <p class="company">Garnet Resale Advisors</p>
  </section>

</body>
</html>
```